Vehicle Artwork to look like emergency response plumber

We need artwork designed for our company fleet, we would like to start with our truck. We would like the vehicle to stand out as an Emergency Response Vehicle (We would like this detailed on the vehicle as well). I have uploaded two different artworks that have been designed by signwriters, however, it looks too busy with not a lot of information. We do all scopes of plumbing and gas works, specialising in Emergency Works. The following could also be listed on the vehicle:
Leak Detection
Burst Pipes
Blocked Drains
Gas Leaks
All Major and Minor Plumbing Works
Industrial, Commercial, Marine, Mining & Domestic
LOGO on Doors must be striped or patterned

Target Market(s)

emergency plumbing works

Industry/Entity Type

Plumbing and gas

Font styles to use
Serif

Colors
EB3D1F
EC4F4E
F09395
F8D3D4
FCEDEE

Requirements
Must have
• company logo rk4619 (in very small font) phone number, emergency response vehicle
Nice to have
• pattern

```html
<!DOCTYPE html>
<html lang="en">
<head>
<meta charset="utf-8">
<title>Emergency Plumbing Response Vehicle – Side Artwork</title>
<link rel="stylesheet" href="https://fonts.googleapis.com/css2?family=Dela+Gothic+One&display=swap">
<style>
  :root {
    --ink: #111111;
    --white: #ffffff;
    --black: #000000;
    --sun: #ffe01a;
    --amber: #f7931e;
    --flame: #e8412b;
    --headline-orange: #f7931e;
    --mark-red: #e03a2c;
    --page: #ffffff;
  }
  html, body {
    margin: 0;
    padding: 0;
    width: 1052px;
    height: 1200px;
    overflow: hidden;
    background: var(--page);
  }
  .canvas {
    position: relative;
    width: 1052px;
    height: 1200px;
  }
  .vehicle-side {
    position: absolute;
    left: 0;
    width: 1052px;
    height: 561px;
  }
  .vehicle-side--driver { top: 22px; }
  .vehicle-side--passenger { top: 605px; }
  .vehicle-side text {
    font-family: "Dela Gothic One", "Arial Black", sans-serif;
  }
  .service-item { font-size: 21px; fill: var(--ink); }
  .bullet { fill: var(--ink); }
  .company-line { font-size: 23px; fill: var(--ink); }
  .headline { font-size: 50px; }
  .headline--accent { fill: var(--headline-orange); }
  .headline--light { fill: var(--white); }
  .phone { font-size: 32px; fill: var(--ink); }
  .response-line { font-size: 40px; fill: var(--ink); }
  .door-name { font-size: 33px; fill: var(--ink); }
  .black-field { fill: var(--black); }
  .brand-square { fill: var(--mark-red); }
</style>
</head>
<body>
<main class="canvas">

  <svg class="vehicle-side vehicle-side--driver" viewBox="0 0 1684 898" aria-label="Driver side vehicle artwork">
    <defs>
      <linearGradient id="warmToRight" x1="0" y1="0" x2="1" y2="0">
        <stop offset="0" stop-color="var(--sun)"/>
        <stop offset="0.55" stop-color="var(--amber)"/>
        <stop offset="1" stop-color="var(--flame)"/>
      </linearGradient>
      <linearGradient id="warmBody" x1="0" y1="0" x2="1" y2="1">
        <stop offset="0" stop-color="var(--amber)"/>
        <stop offset="1" stop-color="#f5a623"/>
      </linearGradient>
    </defs>

    <rect class="services-panel" x="581" y="87" width="964" height="165" fill="url(#warmToRight)"/>
    <rect class="body-panel" x="581" y="252" width="664" height="295" fill="url(#warmBody)"/>
    <path class="black-field" d="M581,252 H848 L878,280 H1035 V483 H870 C820,540 720,560 640,552 C610,548 592,538 581,528 Z"/>
    <rect class="response-band" x="581" y="545" width="1009" height="110" fill="url(#warmToRight)"/>
    <rect class="door-panel" x="107" y="540" width="415" height="113" fill="url(#warmToRight)"/>

    <g class="service-list">
      <circle class="bullet" cx="601" cy="115" r="4"/>
      <text class="service-item" x="622" y="123" textLength="244" lengthAdjust="spacingAndGlyphs">Leak Detection</text>
      <circle class="bullet" cx="601" cy="142" r="4"/>
      <text class="service-item" x="622" y="150" textLength="186" lengthAdjust="spacingAndGlyphs">Burst Pipes</text>
      <circle class="bullet" cx="601" cy="169" r="4"/>
      <text class="service-item" x="622" y="177" textLength="236" lengthAdjust="spacingAndGlyphs">Blocked Drains</text>
      <circle class="bullet" cx="601" cy="196" r="4"/>
      <text class="service-item" x="622" y="204" textLength="166" lengthAdjust="spacingAndGlyphs">Gas Leaks</text>

      <circle class="bullet" cx="910" cy="115" r="4"/>
      <text class="service-item" x="930" y="123" textLength="574" lengthAdjust="spacingAndGlyphs">All Major and Minor Plumbing Works</text>
      <circle class="bullet" cx="910" cy="142" r="4"/>
      <text class="service-item" x="930" y="150" textLength="598" lengthAdjust="spacingAndGlyphs">Industrial, Commercial, Marine, Mining</text>
      <text class="service-item" x="930" y="177" textLength="186" lengthAdjust="spacingAndGlyphs">&amp; Domestic</text>
    </g>
    <text class="company-line" x="1101" y="222" textLength="414" lengthAdjust="spacingAndGlyphs">KESTREL GROUP PTY LTD</text>

    <text class="headline headline--accent" x="617" y="360" textLength="403" lengthAdjust="spacingAndGlyphs">EMERGENCY</text>
    <text class="headline headline--light" x="617" y="416" textLength="331" lengthAdjust="spacingAndGlyphs">PLUMBING</text>
    <text class="headline headline--accent" x="617" y="472" textLength="218" lengthAdjust="spacingAndGlyphs">ORANA</text>
    <rect class="brand-square" x="1100" y="318" width="74" height="74" transform="rotate(45 1137 355)"/>

    <text class="phone" x="880" y="537" textLength="345" lengthAdjust="spacingAndGlyphs">08 5550 0193</text>
    <text class="response-line" x="612" y="598" textLength="555" lengthAdjust="spacingAndGlyphs">24 / 7 EMERGENCY</text>
    <text class="response-line" x="612" y="643" textLength="900" lengthAdjust="spacingAndGlyphs">PLUMBING RESPONSE VEHICLE</text>
    <text class="door-name" x="133" y="613" textLength="374" lengthAdjust="spacingAndGlyphs">KESTREL GROUP</text>
  </svg>

  <svg class="vehicle-side vehicle-side--passenger" viewBox="0 0 1684 898" aria-label="Passenger side vehicle artwork">
    <defs>
      <linearGradient id="warmToLeft" x1="1" y1="0" x2="0" y2="0">
        <stop offset="0" stop-color="var(--sun)"/>
        <stop offset="0.55" stop-color="var(--amber)"/>
        <stop offset="1" stop-color="var(--flame)"/>
      </linearGradient>
      <linearGradient id="warmBodyMirror" x1="1" y1="0" x2="0" y2="1">
        <stop offset="0" stop-color="var(--amber)"/>
        <stop offset="1" stop-color="#f5a623"/>
      </linearGradient>
    </defs>

    <rect class="services-panel" x="140" y="85" width="963" height="167" fill="url(#warmToLeft)"/>
    <rect class="body-panel" x="445" y="252" width="658" height="295" fill="url(#warmBodyMirror)"/>
    <path class="black-field" d="M1103,252 H885 L858,277 H650 V485 H815 C865,532 950,552 1030,549 C1065,546 1090,537 1103,527 Z"/>
    <rect class="response-band" x="95" y="545" width="1008" height="110" fill="url(#warmToLeft)"/>
    <rect class="door-panel" x="1162" y="540" width="415" height="115" fill="url(#warmToLeft)"/>

    <g class="service-list">
      <circle class="bullet" cx="160" cy="107" r="4"/>
      <text class="service-item" x="182" y="115" textLength="244" lengthAdjust="spacingAndGlyphs">Leak Detection</text>
      <circle class="bullet" cx="160" cy="134" r="4"/>
      <text class="service-item" x="182" y="142" textLength="186" lengthAdjust="spacingAndGlyphs">Burst Pipes</text>
      <circle class="bullet" cx="160" cy="161" r="4"/>
      <text class="service-item" x="182" y="169" textLength="236" lengthAdjust="spacingAndGlyphs">Blocked Drains</text>
      <circle class="bullet" cx="160" cy="188" r="4"/>
      <text class="service-item" x="182" y="196" textLength="166" lengthAdjust="spacingAndGlyphs">Gas Leaks</text>

      <circle class="bullet" cx="468" cy="107" r="4"/>
      <text class="service-item" x="490" y="115" textLength="574" lengthAdjust="spacingAndGlyphs">All Major and Minor Plumbing Works</text>
      <circle class="bullet" cx="468" cy="134" r="4"/>
      <text class="service-item" x="490" y="142" textLength="598" lengthAdjust="spacingAndGlyphs">Industrial, Commercial, Marine, Mining</text>
      <text class="service-item" x="490" y="169" textLength="186" lengthAdjust="spacingAndGlyphs">&amp; Domestic</text>
    </g>
    <text class="company-line" x="655" y="207" textLength="416" lengthAdjust="spacingAndGlyphs">KESTREL GROUP PTY LTD</text>

    <rect class="brand-square" x="512" y="320" width="74" height="74" transform="rotate(45 549 357)"/>
    <text class="headline headline--accent" x="677" y="344" textLength="404" lengthAdjust="spacingAndGlyphs">EMERGENCY</text>
    <text class="headline headline--light" x="677" y="400" textLength="332" lengthAdjust="spacingAndGlyphs">PLUMBING</text>
    <text class="headline headline--accent" x="677" y="457" textLength="219" lengthAdjust="spacingAndGlyphs">ORANA</text>

    <text class="phone" x="490" y="532" textLength="345" lengthAdjust="spacingAndGlyphs">08 5550 0193</text>
    <text class="response-line" x="155" y="592" textLength="555" lengthAdjust="spacingAndGlyphs">24 / 7 EMERGENCY</text>
    <text class="response-line" x="155" y="638" textLength="900" lengthAdjust="spacingAndGlyphs">PLUMBING RESPONSE VEHICLE</text>
    <text class="door-name" x="1187" y="614" textLength="374" lengthAdjust="spacingAndGlyphs">KESTREL GROUP</text>
  </svg>

</main>
</body>
</html>
```